Financial Planning firm focused on serving women 55-65 yrs old needs stationary design

We are rebranding our financial planning firm and our target client is a 55-65 yr old women. We need a stationary design to go with our new logo.

Contact Information: Harold Brunsett, MS, CFP President Brunsett Wealth Management 48210 Marlowe Crest Drive, Suite 517 Estero, FL 33928 hal@brunsettwealthgrp.com phone 239-584-0139

```html
<!DOCTYPE html>
<html lang="en">
<head>
<meta charset="utf-8">
<title>Brunsett Wealth Management – Business Cards</title>
<link rel="stylesheet" href="https://fonts.googleapis.com/css2?family=Mulish:wght@400;600;800&display=swap">
<style>
  :root {
    --backdrop: #e4e4e8;
    --navy: #2f5f8a;
    --navy-soft: #3a6a94;
    --forest: #17623a;
    --sage: #a3b6a0;
    --paper: #f1f3f6;
    --ink-grey: #6e7075;
    --faint: rgba(255,255,255,0.07);
  }
  * { box-sizing: border-box; margin: 0; padding: 0; }
  html, body { width: 1200px; height: 934px; overflow: hidden; }
  body {
    background: var(--backdrop);
    font-family: "Mulish", sans-serif;
    position: relative;
  }
  .card {
    position: absolute;
    width: 540px;
    height: 310px;
    overflow: hidden;
    box-shadow: 0 6px 18px rgba(0,0,0,0.12);
  }

  /* Back of card */
  .card-back {
    left: 60px; top: 170px;
    background: var(--navy);
  }
  .card-back .deco-circle {
    position: absolute;
    right: -60px; top: -40px;
    width: 300px; height: 300px;
    border-radius: 50%;
    background: var(--faint);
  }
  .card-back .brand {
    position: absolute;
    left: 70px; top: 110px;
    display: flex; align-items: center; gap: 20px;
  }
  .brand-dot {
    width: 86px; height: 86px; border-radius: 50%;
    background: var(--sage);
    flex: none;
  }
  .brand-name {
    font-weight: 600;
    line-height: 1.05;
    letter-spacing: 0.04em;
    text-transform: uppercase;
  }
  .brand-name .line-main { display: block; font-size: 40px; }
  .brand-name .line-sub { display: block; font-size: 12.5px; letter-spacing: 0.1em; margin-top: 4px; }
  .card-back .brand-name { color: #ffffff; }

  /* Front of card */
  .card-front {
    left: 600px; top: 520px;
    background: var(--paper);
  }
  .card-front .deco-circle {
    position: absolute;
    right: -40px; top: -70px;
    width: 220px; height: 220px;
    border-radius: 50%;
    background: rgba(47,95,138,0.05);
  }
  .card-front .brand {
    position: absolute;
    left: 34px; top: 70px;
    display: flex; align-items: center; gap: 18px;
  }
  .card-front .brand-name { color: var(--navy); }
  .card-front .brand-name .line-main { font-size: 36px; }
  .card-front .brand-name .line-sub { font-size: 11.5px; }

  .contact-person {
    position: absolute;
    right: 26px; top: 112px;
    text-align: right;
  }
  .person-name {
    color: var(--navy);
    font-weight: 800;
    font-size: 15px;
    letter-spacing: 0.03em;
    text-transform: uppercase;
  }
  .person-role {
    color: var(--ink-grey);
    font-size: 11.5px;
    margin-top: 2px;
  }
  .contact-details {
    position: absolute;
    right: 26px; top: 196px;
    text-align: right;
    color: var(--ink-grey);
    font-size: 11px;
    line-height: 1.6;
  }
  .contact-details .label { color: var(--navy); font-weight: 800; }

  .footer-band {
    position: absolute;
    left: 0; right: 0; bottom: 0;
    height: 30px;
    display: flex;
  }
  .footer-band .band-green { width: 32%; background: var(--forest); }
  .footer-band .band-navy { flex: 1; background: var(--navy); }
</style>
</head>
<body>

  <section class="card card-back" aria-label="Business card, reverse side">
    <div class="deco-circle"></div>
    <div class="brand">
      <div class="brand-dot"></div>
      <div class="brand-name">
        <span class="line-main">Brunsett</span>
        <span class="line-sub">Wealth Management</span>
      </div>
    </div>
  </section>

  <section class="card card-front" aria-label="Business card, front side">
    <div class="deco-circle"></div>
    <div class="brand">
      <div class="brand-dot"></div>
      <div class="brand-name">
        <span class="line-main">Brunsett</span>
        <span class="line-sub">Wealth Management</span>
      </div>
    </div>

    <div class="contact-person">
      <p class="person-name">Maren Oakhurst</p>
      <p class="person-role">Managing Director</p>
    </div>

    <div class="contact-details">
      <p>Unit 4, 27 - 33 Linden Avenue, Elmwood VIC 3190</p>
      <p><span class="label">T:</span> (03) 9471 6830 · <span class="label">F:</span> (03) 9471 6831 · <span class="label">E:</span> info@brunsett.com</p>
    </div>

    <div class="footer-band">
      <div class="band-green"></div>
      <div class="band-navy"></div>
    </div>
  </section>

</body>
</html>
```